Design for an exciting fantasy football leaderboard

We are looking for an exciting design for our fantasy football weekly rankings (a leaderboard for player stats & values.) Each day our intelligence engine runs and generates new values for TLB players. The players are then ranked from 1 (best) to something greater (say 40 or 50 players) by a particular position. Our users log in to see the list to help understand player values for their add/drops and to help set their lineups.

Here is an example of the existing page: http://www.pellvane-okra.com/fantasy-football-rankings/weekly-rankings/qb/

Items that we might like to see:
- Our player value (score from 100 HIGH to 1 LOW) worked in
- Some "glory" stats - rushing yards, rushing TDs, opportunities (for RBs as an example) worked into the table
- A better way to share statistical movement of the players value
- A way to use icons (and some icons) to show special player call outs
- Improved UI for the buttons to navigate to other positions and scoring systems
- A design call out that highlights that each player name can be clicked to go to the player page
- A small call out box that describes that our engine is working and why it is cool
- A date last processed that is not overwhelming but noticeable
- A sense of energy and movement. This should be a fun and exciting view

Feel free to email with questions or thoughts

What we'd like is a more exciting format that uses icons and imagery to denote players who are rising, falling, hot, cold, injured, etc.

This is our test run of Mosaic Hatch. We have a lot of similar projects that we would like to work on in 2014. Each year our off-season begins on JAN 1 - so we are excited to begin working. If we can find a designer or two that understands the visual energy of fantasy football and can pickup our brand from the existing site - we'll have more work.
Updates

We've updated the project to be payment guaranteed.  We hope that will show that we are serious about working with Mosaic Hatch designers in 2014 on a variety of projects.

I'd like to thank everyone who participated in the contest.  It was a pleasure to work with all of you and I thank you for taking the time to work on our project.   I am confident that we will see you again in the future with additional contests!

Target Market(s)

We are building a new brand around fantasy football analytics - our audience cares greatly about getting detailed analysis for their fantasy football teams. The look should be professional in appearance (nothing cartoony) and be easy to read. Our audience is primarily male...educated beyond high school.

Check out our site as it is today: http://www.pellvane-okra.com. Our preseason designs are stronger than the weekly rankings. For instance, we all liked the design of this page: http://www.pellvane-okra.com/2013-fantasy-football-rankings/projections/rb/

Requirements
Must have
• - Improved UX for the page and the sub navigation
- Must fit and work well on tablets and normal PCs
- Rankings should be easy to read and well laid out
- Clean, professional design
Nice to have
• - Sense of movement and momentum...these players are moving up and down daily and that is important to our users
- Icons for Rising, Falling, Sleeper, Suggested Waiver claim, Hot, Cold, etc
- Sense of excitement...avoid the wall of words
- Possibly a cool "light box" window that gives more info about the player if someone rolls over the name, or taps a "more info" icon. If someone clicks the "go to player page" in the light box then they would surf to the player page.
Should not have
• - Cliché football icons or pictures of turf fields
- Comic sans font
- Soccer imagery - this is TLB American Football

```html
<!DOCTYPE html>
<html lang="en">
<head>
<meta charset="utf-8">
<title>Weekly QB Rankings</title>
<link rel="stylesheet" href="https://fonts.googleapis.com/css2?family=Open+Sans:wght@400;600;700&display=swap">
<style>
  :root {
    --stage: #d9dce0;
    --panel: #ffffff;
    --stats-bar: #3a3d42;
    --cell-grey: #ececee;
    --rank-green: #7cc06a;
    --text-dark: #4a4a4a;
    --text-muted: #a9a9a9;
    --label-light: #ffffff;
    --stat-label: #a3a6ab;
    --hot: #f0623c;
    --rise: #7cc06a;
    --fall: #ee5a3a;
    --bar-track: #e6e6e6;
    --bar-start: #6fcb3c;
    --bar-end: #ffe21a;
    --band-gold: #c4a574;
    --band-navy: #0f3a57;
    --band-blue: #0b2d5b;
    --band-green: #27443a;
    --band-cyan: #0096c8;
  }
  * { box-sizing: border-box; margin: 0; padding: 0; }
  html, body { width: 1200px; height: 683px; overflow: hidden; }
  body {
    background: var(--stage);
    font-family: "Open Sans", Arial, sans-serif;
    position: relative;
  }
  .leaderboard {
    position: absolute;
    left: 132px; top: 88px;
    width: 935px; height: 507px;
    background: var(--panel);
    box-shadow: 0 6px 30px rgba(0,0,0,0.18);
    padding: 17px 0 0 15px;
  }
  .player-row {
    position: relative;
    width: 905px; height: 74px;
    margin-bottom: 23px;
    box-shadow: 0 2px 2px rgba(0,0,0,0.08);
  }
  .row-head {
    height: 20px;
    border-radius: 3px 3px 0 0;
    color: var(--label-light);
    font-size: 10px;
    position: relative;
  }
  .row-head span { position: absolute; top: 4px; }
  .row-main { height: 30px; background: #fff; position: relative; }
  .row-stats {
    height: 24px; background: var(--stats-bar);
    position: relative; font-size: 10px; color: var(--stat-label);
  }
  .row-stats span { position: absolute; top: 6px; }
  .row-stats b { color: #fff; font-weight: 700; margin-left: 5px; }
  .gold .row-head { background: var(--band-gold); }
  .navy .row-head { background: var(--band-navy); }
  .blue .row-head { background: var(--band-blue); }
  .green .row-head { background: var(--band-green); }
  .cyan .row-head { background: var(--band-cyan); }

  .rank-badge {
    position: absolute; left: 0; top: 20px;
    width: 33px; height: 34px;
    background: var(--rank-green);
    color: #fff; font-weight: 700; font-size: 22px;
    display: flex; align-items: center; justify-content: center;
    border-radius: 0 2px 2px 0;
    z-index: 2;
  }
  .avatar {
    position: absolute; left: 44px; top: 2px;
    width: 67px; height: 67px; border-radius: 50%;
    border: 3px solid #fff;
    background: radial-gradient(circle at 50% 40%, #d7b9a2 0%, #b89683 45%, #8f8a87 100%);
    box-shadow: 0 0 0 1px #d0d0d0;
    z-index: 2;
  }
  .pos-chip {
    position: absolute; left: 139px; top: 5px;
    width: 22px; height: 22px; border-radius: 50%;
    background: #e4e4e4; color: var(--text-muted);
    font-size: 9px; font-weight: 600;
    display: flex; align-items: center; justify-content: center;
  }
  .player-name {
    position: absolute; left: 192px; top: 4px;
    font-size: 16px; font-weight: 600; color: var(--text-dark);
  }
  .team-cell {
    position: absolute; left: 397px; top: 0; width: 125px; height: 30px;
    background: var(--cell-grey);
    font-size: 16px; font-weight: 600; color: var(--text-dark);
    padding: 4px 0 0 7px;
  }
  .status-icons { position: absolute; left: 556px; top: 7px; display: flex; gap: 14px; }
  .move-cell {
    position: absolute; left: 670px; top: 0; width: 82px; height: 30px;
    background: var(--cell-grey);
    color: var(--text-dark); padding: 4px 0 0 14px;
    font-size: 16px; font-weight: 600;
    display: flex; align-items: baseline; gap: 4px;
  }
  .move-cell small { font-size: 10px; font-weight: 600; }
  .move-cell svg { align-self: center; margin-top: 2px; }
  .value-num {
    position: absolute; left: 781px; top: 4px;
    font-size: 16px; font-weight: 600; color: var(--text-dark);
  }
  .value-bar {
    position: absolute; left: 803px; top: 9px; width: 92px; height: 13px;
    background: var(--bar-track); border-radius: 7px; overflow: hidden;
  }
  .value-bar i {
    display: block; height: 100%; border-radius: 7px;
    background: linear-gradient(90deg, var(--bar-start), var(--bar-end));
  }
</style>
</head>
<body>
<svg width="0" height="0" style="position:absolute">
  <defs>
    <symbol id="icon-hot" viewBox="0 0 12 16"><path d="M6 0c1 3 5 5 5 10a5 5 0 0 1-10 0c0-2 1-3 2-4 0 2 1 3 2 3-1-3 0-6 1-9zM6 9c-1 1-2 2-2 4a2 2 0 0 0 4 0c0-2-1-3-2-4z" fill="var(--hot)"/></symbol>
    <symbol id="icon-rising" viewBox="0 0 16 16"><path d="M8 1l7 7H1z" fill="var(--hot)"/><rect x="1" y="10" width="14" height="1.5" fill="var(--hot)"/><rect x="1" y="13" width="14" height="1.5" fill="var(--hot)"/></symbol>
    <symbol id="arrow-up" viewBox="0 0 12 14"><path d="M6 0l6 7H8v7H4V7H0z" fill="var(--rise)"/></symbol>
    <symbol id="arrow-down" viewBox="0 0 12 14"><path d="M6 14l6-7H8V0H4v7H0z" fill="var(--fall)"/></symbol>
  </defs>
</svg>

<main class="leaderboard">
  <section class="player-row gold">
    <div class="row-head"><span style="left:5px">Rank</span><span style="left:132px">Position</span><span style="left:192px">Player</span><span style="left:400px">Team</span><span style="left:548px">Status</span><span style="left:677px">Movement</span><span style="left:766px">Value</span></div>
    <div class="rank-badge">1</div>
    <div class="avatar" role="img" aria-label="Headshot of quarterback Dale Brennick"></div>
    <div class="row-main">
      <div class="pos-chip">QB</div>
      <div class="player-name">Dale Brennick</div>
      <div class="team-cell">Harriers</div>
      <div class="status-icons"><svg width="12" height="16"><use href="#icon-hot"/></svg><svg width="15" height="15"><use href="#icon-rising"/></svg></div>
      <div class="move-cell">5 <small>places</small><svg width="11" height="13"><use href="#arrow-up"/></svg></div>
      <div class="value-num">98</div>
      <div class="value-bar"><i style="width:91%"></i></div>
    </div>
    <div class="row-stats"><span style="left:137px">Stats:</span><span style="left:174px">RY<b>150</b></span><span style="left:231px">RTD<b>4</b></span><span style="left:285px">LG<b>39</b></span><span style="left:406px">Ts:<b>2nd Overall</b></span></div>
  </section>

  <section class="player-row navy">
    <div class="row-head"><span style="left:5px">Rank</span><span style="left:132px">Position</span><span style="left:192px">Player</span><span style="left:400px">Team</span><span style="left:548px">Status</span><span style="left:677px">Movement</span><span style="left:766px">Value</span></div>
    <div class="rank-badge">2</div>
    <div class="avatar" role="img" aria-label="Headshot of quarterback Preston Marlow"></div>
    <div class="row-main">
      <div class="pos-chip">QB</div>
      <div class="player-name">Preston Marlow</div>
      <div class="team-cell">Comets</div>
      <div class="status-icons"><svg width="12" height="16"><use href="#icon-hot"/></svg><svg width="15" height="15"><use href="#icon-rising"/></svg></div>
      <div class="move-cell">1 <small>place</small><svg width="11" height="13"><use href="#arrow-down"/></svg></div>
      <div class="value-num">95</div>
      <div class="value-bar"><i style="width:86%"></i></div>
    </div>
    <div class="row-stats"><span style="left:137px">Stats:</span><span style="left:174px">RY<b>119</b></span><span style="left:231px">RTD<b>4</b></span><span style="left:285px">LG<b>17</b></span><span style="left:406px">Ts:<b>1st Overall</b></span></div>
  </section>

  <section class="player-row blue">
    <div class="row-head"><span style="left:5px">Rank</span><span style="left:132px">Position</span><span style="left:192px">Player</span><span style="left:400px">Team</span><span style="left:548px">Status</span><span style="left:677px">Movement</span><span style="left:766px">Value</span></div>
    <div class="rank-badge">3</div>
    <div class="avatar" role="img" aria-label="Headshot of quarterback Tod Brandell"></div>
    <div class="row-main">
      <div class="pos-chip">QB</div>
      <div class="player-name">Tod Brandell</div>
      <div class="team-cell">Foxes</div>
      <div class="status-icons"><svg width="12" height="16"><use href="#icon-hot"/></svg><svg width="15" height="15"><use href="#icon-rising"/></svg></div>
      <div class="move-cell">1 <small>place</small><svg width="11" height="13"><use href="#arrow-down"/></svg></div>
      <div class="value-num">92</div>
      <div class="value-bar"><i style="width:83%"></i></div>
    </div>
    <div class="row-stats"><span style="left:137px">Stats:</span><span style="left:174px">RY<b>98</b></span><span style="left:231px">RTD<b>3</b></span><span style="left:285px">LG<b>15</b></span><span style="left:406px">Ts:<b>4st Overall</b></span></div>
  </section>

  <section class="player-row green">
    <div class="row-head"><span style="left:5px">Rank</span><span style="left:132px">Position</span><span style="left:192px">Player</span><span style="left:400px">Team</span><span style="left:548px">Status</span><span style="left:677px">Movement</span><span style="left:766px">Value</span></div>
    <div class="rank-badge">4</div>
    <div class="avatar" role="img" aria-label="Headshot of quarterback Alden Rourke"></div>
    <div class="row-main">
      <div class="pos-chip">QB</div>
      <div class="player-name">Alden Rourke</div>
      <div class="team-cell">Foxes</div>
      <div class="status-icons"><svg width="12" height="16"><use href="#icon-hot"/></svg><svg width="15" height="15"><use href="#icon-rising"/></svg></div>
      <div class="move-cell">3 <small>places</small><svg width="11" height="13"><use href="#arrow-up"/></svg></div>
      <div class="value-num">89</div>
      <div class="value-bar"><i style="width:76%"></i></div>
    </div>
    <div class="row-stats"><span style="left:137px">Stats:</span><span style="left:174px">RY<b>92</b></span><span style="left:231px">RTD<b>3</b></span><span style="left:285px">LG<b>11</b></span><span style="left:406px">Ts:<b>5th Overall</b></span></div>
  </section>

  <section class="player-row cyan">
    <div class="row-head"><span style="left:5px">Rank</span><span style="left:132px">Position</span><span style="left:192px">Player</span><span style="left:400px">Team</span><span style="left:548px">Status</span><span style="left:677px">Movement</span><span style="left:766px">Value</span></div>
    <div class="rank-badge">5</div>
    <div class="avatar" role="img" aria-label="Headshot of quarterback Cal Norwood"></div>
    <div class="row-main">
      <div class="pos-chip">QB</div>
      <div class="player-name">Cal Norwood</div>
      <div class="team-cell">Foxes</div>
      <div class="status-icons"><svg width="12" height="16"><use href="#icon-hot"/></svg><svg width="15" height="15"><use href="#icon-rising"/></svg></div>
      <div class="move-cell">1 <small>place</small><svg width="11" height="13"><use href="#arrow-up"/></svg></div>
      <div class="value-num">88</div>
      <div class="value-bar"><i style="width:75%"></i></div>
    </div>
    <div class="row-stats"><span style="left:137px">Stats:</span><span style="left:174px">RY<b>85</b></span><span style="left:231px">RTD<b>3</b></span><span style="left:285px">LG<b>12</b></span><span style="left:406px">Ts:<b>8th Overall</b></span></div>
  </section>
</main>
</body>
</html>
```